I need a new design for my real estate signage!

Would like a new design for my real estate signs. I do have a logo that needs to be used along with the word AVAILABLE and my phone number 505-718-2094

Target Market(s)

Real estate buyers and sellers

Industry/Entity Type

Real Estate

Font styles to use
Serif

Colors
000000

Requirements
Must have
• Company name phone number
• Colors: turquoise, white black
Nice to have
• Modern design

```html
<!DOCTYPE html>
<html lang="en">
<head>
<meta charset="utf-8">
<title>Corvalle Real Estate Services – Sign</title>
<link rel="stylesheet" href="https://fonts.googleapis.com/css2?family=Cinzel:wght@600&family=Open+Sans:wght@700&display=swap">
<style>
  :root {
    --night-deep: #080d14;
    --night-glow: #2b3d52;
    --copper-dark: #7d4526;
    --copper-mid: #c27d52;
    --copper-light: #f1bb94;
    --turquoise: #14aebf;
    --turquoise-shade: #0b8593;
    --sign-white: #ffffff;
  }
  html, body {
    margin: 0;
    padding: 0;
    width: 1200px;
    height: 540px;
    overflow: hidden;
    background: var(--night-deep);
  }
  .sign-canvas {
    display: block;
    width: 1200px;
    height: 540px;
  }
  .company-name {
    font-family: "Cinzel", serif;
    font-weight: 600;
    fill: var(--sign-white);
  }
  .tagline, .phone-number, .brand-wordmark {
    font-family: "Open Sans", sans-serif;
    font-weight: 700;
    fill: var(--sign-white);
  }
</style>
</head>
<body>
<svg class="sign-canvas" viewBox="0 0 900 405" xmlns="http://www.w3.org/2000/svg" role="img" aria-label="Corvalle Real Estate Services sign">
  <defs>
    <radialGradient id="night-backdrop" cx="50%" cy="45%" r="60%">
      <stop offset="0" stop-color="var(--night-glow)"/>
      <stop offset="1" stop-color="var(--night-deep)"/>
    </radialGradient>
    <linearGradient id="copper" x1="0" y1="0" x2="1" y2="0">
      <stop offset="0" stop-color="var(--copper-dark)"/>
      <stop offset="0.2" stop-color="var(--copper-mid)"/>
      <stop offset="0.45" stop-color="var(--copper-light)"/>
      <stop offset="0.7" stop-color="var(--copper-mid)"/>
      <stop offset="1" stop-color="var(--copper-dark)"/>
    </linearGradient>
    <linearGradient id="copper-vertical" x1="0" y1="0" x2="0" y2="1">
      <stop offset="0" stop-color="var(--copper-light)"/>
      <stop offset="1" stop-color="var(--copper-dark)"/>
    </linearGradient>
    <radialGradient id="panel-fill" cx="50%" cy="50%" r="65%">
      <stop offset="0.75" stop-color="var(--turquoise)"/>
      <stop offset="1" stop-color="var(--turquoise-shade)"/>
    </radialGradient>
  </defs>

  <rect class="backdrop" width="900" height="405" fill="url(#night-backdrop)"/>

  <!-- posts -->
  <g class="sign-posts" fill="url(#copper)">
    <rect x="222" y="350" width="36" height="55"/>
    <rect x="684" y="350" width="36" height="55"/>
  </g>

  <!-- frame body -->
  <path class="sign-frame" d="M125,98 Q462,48 800,98 L800,338 L125,338 Z" fill="url(#copper)"/>

  <!-- arched cap bands -->
  <g class="sign-cap" fill="url(#copper)">
    <path d="M107,86 Q458,26 808,86 L808,94 Q458,34 107,94 Z"/>
    <path d="M111,94 Q458,34 804,94 L804,101 Q458,42 111,101 Z" opacity="0.9"/>
    <path d="M116,101 Q458,42 799,101 L799,108 Q458,50 116,108 Z"/>
  </g>

  <!-- base bar -->
  <rect class="sign-base" x="115" y="335" width="685" height="17" fill="url(#copper-vertical)"/>

  <!-- turquoise panel -->
  <path class="sign-panel" d="M143,110 Q463,60 783,110 L783,318 L143,318 Z" fill="url(#panel-fill)" stroke="var(--turquoise-shade)" stroke-width="2"/>

  <!-- brand mark stand-in -->
  <g class="brand-mark">
    <circle cx="407" cy="118" r="6" fill="var(--sign-white)"/>
    <text class="brand-wordmark" x="420" y="124" font-size="17">CORVALLE</text>
  </g>

  <text class="company-name" x="458" y="235" font-size="76" text-anchor="middle" textLength="336" lengthAdjust="spacingAndGlyphs">CORVALLE</text>

  <text class="tagline" x="454" y="271" font-size="27" text-anchor="middle" textLength="338" lengthAdjust="spacingAndGlyphs">REAL ESTATE SERVICES</text>

  <!-- phone -->
  <g class="phone-line">
    <g class="phone-icon" fill="none" stroke="var(--sign-white)" stroke-width="2">
      <path d="M346,292 Q359,282 372,292 L370,297 L364,295 L364,292 L354,292 L354,295 L348,297 Z" fill="var(--sign-white)"/>
      <path d="M352,296 L349,307 L369,307 L366,296 Z"/>
      <circle cx="359" cy="301.5" r="3"/>
    </g>
    <text class="phone-number" x="381" y="307" font-size="22" textLength="176" lengthAdjust="spacingAndGlyphs">505-718-2094</text>
  </g>
</svg>
</body>
</html>
```